【画像サイズ】※MZSより抜粋
表紙ファイルの理想的な採寸は2,560×1,600ピクセルです。
注:画像の寸法は1,000×625ピクセル以上であることが必要です。
画像の最大の寸法は10,000×10,000ピクセルです。

【タイトル】
家族向け専任相談員がすすめる日々の工夫
ドキドキ平気!まあるい毎日の育ち術

サブキャッチ
心理学×四柱推命メソッド
我が子を上手に愛したいあなたへ

【著者】
ひだまりファミリーケア協会 もりした かなえ

【本の内容】
子どもを怒って、自分を責めてしまうお母様向けです。
子育ての悩みを、育児書やインターネット情報では効果がなかったり
どちらにも相談できなかったりする現状。
心理学×四柱推命メソッドで、お母様とお子様だけの簡単な解決方法を
やさしくお伝えします。
子どもと過ごすのが楽しくなり、母子ともに満たされ笑顔・Happyな暮らしを実現します。

※本文を参考資料として添付いたします。

【デザイン要望】
タイトル、サブキャッチと合わせて
読者様特典プレゼントのアピールもしたいです。

読者様特典として、イラストでやさしくわかりやすい!四柱推命電子書籍プレゼント

特にイメージにこだわりはありませんので、
自由な発想でのデザインご応募を楽しみにしております。

※次点、次々点の方への参加報酬を設定いたしました。

※その他、必要な情報がありましたら、お問い合わせください。
どうぞ、よろしくお願いいたします。

依頼のジャンルは、子育て・母親向け・育児法・心理学・学び・カウンセリング です。
カテゴリーに近いものがなく、ひとまず、資格・習い事としております。

優しい色使いと、見やすいタイトル、まとまり感でこちらに決定いたしました。

たくさんの素晴らしい商品にに感動しました。本当にありがとうございました。どちらも選びたくて本当に、迷いに迷いました。

```html
<!DOCTYPE html>
<html lang="ja">
<head>
<meta charset="utf-8">
<title>ドキドキ平気!まあるい毎日の育ち術</title>
<link href="https://fonts.googleapis.com/css2?family=Zen+Maru+Gothic:wght@500;700;900&display=swap" rel="stylesheet">
<style>
  :root {
    --bg-pink: #f2c7c1;
    --paper: #fffdfb;
    --ink-brown: #5b3b33;
    --accent-red: #b8464c;
    --teal: #5fb0b3;
    --figure-pink: #e79a9a;
    --figure-blue: #bfe0e4;
  }
  * { margin: 0; padding: 0; box-sizing: border-box; }
  html, body { width: 749px; height: 1200px; overflow: hidden; }
  body {
    background: var(--bg-pink);
    font-family: "Zen Maru Gothic", sans-serif;
    color: var(--ink-brown);
  }
  .cover {
    position: relative;
    width: 749px;
    height: 1200px;
    overflow: hidden;
    background: var(--bg-pink);
  }
  .title-disc {
    position: absolute;
    left: 40px; top: 30px;
    width: 560px; height: 560px;
    border-radius: 50%;
    background: var(--paper);
  }
  .kicker {
    position: absolute;
    left: 40px; top: 112px; width: 570px;
    text-align: center;
    font-size: 18px; font-weight: 700;
    white-space: nowrap;
  }
  .title {
    position: absolute;
    left: 40px; top: 200px; width: 570px;
    text-align: center;
    font-weight: 900;
    line-height: 1;
    white-space: nowrap;
  }
  .title .line1 { display: block; font-size: 68px; }
  .title .line2 { display: block; font-size: 74px; color: var(--teal); margin-top: 40px; }
  .title .line3 { display: block; font-size: 64px; margin-top: 42px; }
  .subcatch-method,
  .subcatch-reader {
    position: absolute;
    writing-mode: vertical-rl;
    font-weight: 900;
    white-space: nowrap;
  }
  .subcatch-method {
    top: 48px; right: 26px;
    font-size: 30px;
    color: var(--accent-red);
  }
  .subcatch-reader {
    top: 98px; right: 74px;
    font-size: 20px;
    letter-spacing: 1px;
  }
  .figure {
    position: absolute;
    left: 30px; top: 600px;
    width: 360px; height: 570px;
    border-radius: 180px 180px 120px 60px;
    background: linear-gradient(180deg, var(--figure-pink) 0%, var(--figure-pink) 32%, var(--figure-blue) 33%, #d7ecef 100%);
  }
  .author {
    position: absolute;
    left: 350px; top: 656px; width: 380px;
    text-align: center;
    white-space: nowrap;
  }
  .author .org { font-size: 18px; font-weight: 700; }
  .author .name { font-size: 40px; font-weight: 900; letter-spacing: 6px; margin-top: 12px; }
  .bonus {
    position: absolute;
    left: 405px; top: 785px;
    width: 350px; height: 350px;
    border-radius: 50%;
    background: var(--paper);
    text-align: center;
    padding-top: 38px;
    white-space: nowrap;
  }
  .bonus::before {
    content: "";
    position: absolute;
    inset: 12px;
    border-radius: 50%;
    border: 2px dashed var(--bg-pink);
  }
  .bonus .label { font-size: 36px; font-weight: 900; letter-spacing: 2px; }
  .bonus .rule { display: block; width: 230px; height: 2px; background: var(--ink-brown); margin: 12px auto 16px; }
  .bonus .lead { font-size: 17px; font-weight: 700; color: var(--teal); }
  .bonus .gift { font-size: 32px; font-weight: 900; line-height: 1.6; margin-top: 14px; }
</style>
</head>
<body>
<main class="cover">
  <div class="title-disc"></div>
  <p class="kicker">家族向け専任相談員がすすめる日々の工夫</p>
  <h1 class="title">
    <span class="line1">ドキドキ平気!</span>
    <span class="line2">まあるい毎日</span>
    <span class="line3">の育ち術</span>
  </h1>
  <p class="subcatch-method">心理学×四柱推命メソッド</p>
  <p class="subcatch-reader">我が子を上手に愛したいあなたへ</p>
  <div class="figure" role="img" aria-label="赤ちゃんを抱きしめる母親のやさしいイラスト"></div>
  <div class="author">
    <p class="org">ひだまりファミリーケア協会</p>
    <p class="name">もりした かなえ</p>
  </div>
  <section class="bonus">
    <p class="label">読者様特典</p>
    <span class="rule"></span>
    <p class="lead">イラストでやさしくわかりやすい!</p>
    <p class="gift">四柱推命電子書籍<br>プレゼント</p>
  </section>
</main>
</body>
</html>
```